Business card for medical clinic

I need an upmarket, modern medical/health business card for my clinic

Contact Information for Business Card

name, address, email, qr code

```html
<!DOCTYPE html>
<html lang="en">
<head>
<meta charset="UTF-8">
<title>Lumera Health Partners – Business Card</title>
<link rel="stylesheet" href="https://fonts.googleapis.com/css2?family=Poppins:wght@300;400;600&display=swap">
<style>
  :root {
    --stage: #232325;
    --card-dark: #202023;
    --card-blue: #29a6de;
    --accent: #29a3dc;
    --ink-light: #ffffff;
    --brand-on-blue: #dff2fb;
    --rule: #1e86b8;
  }
  * { box-sizing: border-box; margin: 0; padding: 0; }
  html, body {
    width: 1200px; height: 780px; overflow: hidden;
    background: var(--stage);
    font-family: "Poppins", sans-serif;
  }
  .stage {
    width: 1200px; height: 780px;
    display: flex; align-items: center; justify-content: center; gap: 40px;
  }
  .card {
    width: 540px; height: 309px;
    position: relative; overflow: hidden;
    box-shadow: 0 14px 30px rgba(0,0,0,.45);
  }
  .card--front { background: var(--card-dark); display: flex; }
  .card--back { background: var(--card-blue); display: flex; align-items: center; justify-content: center; }

  .brand {
    display: flex; align-items: center; gap: 12px;
    font-weight: 400; letter-spacing: .06em; text-transform: uppercase; line-height: 1.15;
  }
  .brand__dot { border-radius: 50%; flex: none; }
  .brand--front { color: var(--accent); font-size: 15px; }
  .brand--front .brand__dot { width: 14px; height: 14px; background: var(--accent); }
  .brand--back { color: var(--brand-on-blue); font-size: 28px; }
  .brand--back .brand__dot { width: 26px; height: 26px; background: var(--brand-on-blue); }

  .front__logo-area {
    width: 250px; display: flex; align-items: center; justify-content: center;
  }
  .front__divider { width: 1px; background: var(--rule); margin: 52px 0; }
  .front__details {
    flex: 1; padding: 48px 0 0 34px;
  }
  .person__name { font-size: 30px; line-height: 1.05; color: var(--accent); }
  .person__first { font-weight: 600; }
  .person__last { font-weight: 300; }
  .person__title { font-size: 13px; color: var(--ink-light); margin-top: 4px; }
  .address { margin-top: 16px; font-size: 12.5px; color: var(--accent); line-height: 1.45; }
  .contacts { list-style: none; margin-top: 16px; }
  .contacts li {
    display: flex; align-items: center; gap: 10px;
    font-size: 12.5px; color: var(--ink-light); line-height: 1.75;
  }
  .contacts svg { width: 13px; height: 13px; flex: none; }
</style>
</head>
<body>
<main class="stage">
  <section class="card card--front" aria-label="Business card front">
    <div class="front__logo-area">
      <div class="brand brand--front">
        <span class="brand__dot"></span>
        <span>Lumera Health<br>Partners</span>
      </div>
    </div>
    <div class="front__divider"></div>
    <div class="front__details">
      <h1 class="person__name"><span class="person__first">Marta</span> <span class="person__last">Kovalenko</span></h1>
      <p class="person__title">Founder &amp; CEO</p>
      <p class="address">410 Cedarbrook Ave. Suite 120<br>Austin, TX 78704</p>
      <ul class="contacts">
        <li>
          <svg viewBox="0 0 24 24" aria-hidden="true"><path fill="#29a3dc" d="M6.6 10.8a15.1 15.1 0 0 0 6.6 6.6l2.2-2.2a1 1 0 0 1 1-.25 11.4 11.4 0 0 0 3.6.57 1 1 0 0 1 1 1V20a1 1 0 0 1-1 1A17 17 0 0 1 3 4a1 1 0 0 1 1-1h3.5a1 1 0 0 1 1 1c0 1.25.2 2.45.57 3.57a1 1 0 0 1-.25 1z"/></svg>
          (512) 555-0148
        </li>
        <li>
          <svg viewBox="0 0 24 24" aria-hidden="true"><rect x="2" y="5" width="20" height="14" rx="2" fill="#29a3dc"/><path d="M3 6l9 7 9-7" fill="none" stroke="#202023" stroke-width="1.8"/></svg>
          hello@lumerahealth.com
        </li>
        <li>
          <svg viewBox="0 0 24 24" aria-hidden="true"><circle cx="12" cy="12" r="10" fill="#29a3dc"/><path d="M2 12h20M12 2c3 3 3 17 0 20M12 2c-3 3-3 17 0 20" fill="none" stroke="#202023" stroke-width="1.5"/></svg>
          www.lumerahealth.com
        </li>
      </ul>
    </div>
  </section>

  <section class="card card--back" aria-label="Business card back">
    <div class="brand brand--back">
      <span class="brand__dot"></span>
      <span>Lumera Health<br>Partners</span>
    </div>
  </section>
</main>
</body>
</html>
```